New company branded Power Point Template for presentations

We would like to have a clean and professional PowerPoint template made for our rebranding effort. It will be for our main company (Gordavexa) and will be used for both general introductory presentations and more technical industry related webinar and in-person presentations. We are a company in the manufacturing space working primarily in automotive. We provide simulation services to optimize production and softwares to allow users to do the same for themselves. The template needs to be easy to modify (even for novice users). I would like a good cover slide, content slides with common title / logo / etc. and a Q&A slide along with a final slide "Thank you" of similar. I have included our brand style guide in a high res pdf. Its images should be sufficient but please let me know if that is not the case.

```html
<!DOCTYPE html>
<html lang="en">
<head>
<meta charset="utf-8">
<title>Gordavexa Presentation Template</title>
<link href="https://fonts.googleapis.com/css2?family=Exo+2:wght@600;700&family=Figtree:wght@400;500;600&display=swap" rel="stylesheet">
<style>
:root{
  --teal:#1b7f94;
  --orange:#e69a13;
  --ink:#121417;
  --navy:#17344a;
  --grey:#d9dcdf;
  --paper:#ffffff;
}
*{margin:0;padding:0;box-sizing:border-box}
html,body{width:1036px;height:1200px;overflow:hidden;background:var(--paper)}
body{position:relative;font-family:"Figtree",Arial,sans-serif;color:var(--ink)}
.slide{position:absolute;width:427px;height:240px;background:var(--paper);overflow:hidden;
  box-shadow:0 6px 18px rgba(0,0,0,.28)}
.col-l{left:65px}.col-r{left:542px}
.row-1{top:41px}.row-2{top:322px}.row-3{top:610px}.row-4{top:891px}
.abs{position:absolute}
.bar-top{position:absolute;top:0;right:0;left:209px;height:3px;background:var(--teal)}
.bar-side{position:absolute;left:0;top:115px;bottom:0;width:3px;background:var(--orange)}
.brand{position:absolute;left:22px;top:22px;display:flex;align-items:center;gap:5px;
  font-family:"Exo 2",sans-serif;font-weight:700;font-size:10px;letter-spacing:.09em;color:var(--navy)}
.brand i{display:block;width:13px;height:13px;background:var(--teal)}
.headline{font-family:"Exo 2",sans-serif;font-weight:700;text-transform:uppercase;color:var(--ink);letter-spacing:.01em}
.hl-teal{color:var(--teal)}.hl-orange{color:var(--orange)}
.tag-label{position:absolute;right:22px;top:26px;font-family:"Figtree",sans-serif;font-weight:600;font-size:10px;
  color:var(--teal);padding-bottom:3px;border-bottom:1.5px solid var(--grey);text-transform:uppercase}
.center{text-align:center;left:0;right:0}
.photo{position:absolute}
.frame{position:absolute;overflow:visible}

/* cover */
.cover-side{position:absolute;left:0;top:0;width:3px;height:208px;background:var(--orange)}
.cover-bottom{position:absolute;left:21px;bottom:0;width:196px;height:3px;background:var(--teal)}
.cover .brand{left:22px;top:40px;font-size:15px;gap:8px}
.cover .brand i{width:24px;height:24px}
.cover-title{left:22px;top:93px;font-size:16.5px;line-height:19px}
.cover-sub{left:22px;top:158px;font-size:9px;line-height:13.5px;font-weight:500}

/* toc */
.toc-title{top:76px;font-size:18px}
.toc-row{position:absolute;left:108px;width:204px;display:flex;justify-content:space-between;font-size:8.5px;font-weight:500}
.toc-row b{color:var(--teal);font-weight:600}

/* agenda */
.section-title{top:58px;font-size:18px}
.time-tag{position:absolute;top:96px;width:56px;height:39px;background:var(--teal);color:#fff;
  clip-path:polygon(0 0,100% 0,100% 72%,80% 100%,0 100%);
  font-weight:700;font-size:8px;line-height:10.5px;text-align:center;padding-top:9px}
.agenda-item{position:absolute;top:148px;width:100px;text-align:center}
.agenda-item h3{font-weight:500;font-size:8.5px;line-height:10.5px;margin-bottom:5px}
.agenda-item p{font-size:4.6px;line-height:7.6px}

/* who we are */
.who-title{top:152px;font-size:17.5px}
.body-center{position:absolute;left:40px;right:40px;text-align:center;font-size:6px;line-height:10.6px;font-weight:500}

/* goals */
.icon-box{position:absolute;top:132px;width:55px;height:39px}
.goal-label{position:absolute;top:183px;width:90px;text-align:center;font-weight:500;font-size:8.5px;line-height:10.8px}

/* q&a */
.qa-num{position:absolute;left:37px;top:108px;width:31px;height:27px;background:var(--teal);color:#fff;
  font-family:"Exo 2",sans-serif;font-weight:700;font-size:12.5px;text-align:center;line-height:27px}
.qa-q{position:absolute;left:83px;top:103px;width:255px;font-size:9.5px;line-height:17px;font-weight:500}
.qa-rule{position:absolute;left:83px;top:151px;width:259px;height:1px;background:var(--grey)}
.qa-a{position:absolute;left:83px;top:162px;width:262px;font-size:5.9px;line-height:10.7px;font-weight:500}

/* advantage */
.adv-panel{position:absolute;left:124px;top:0;width:279px;height:128px}
.adv-title{left:156px;top:19px;font-size:17.5px;line-height:22px}
.adv-body{left:156px;top:70px;width:236px;font-size:5.9px;line-height:10.7px;font-weight:500}

/* thanks */
.thanks-title{left:22px;top:57px;font-size:17.5px;line-height:22px;width:400px}
.contact-head{left:22px;top:139px;font-size:10px;font-weight:600;color:var(--orange)}
.contact-line{position:absolute;left:22px;display:flex;align-items:center;gap:7px;font-size:6px;font-weight:500}
</style>
</head>
<body>

<!-- Cover -->
<section class="slide col-l row-1 cover">
  <div class="cover-side"></div>
  <div class="brand"><i></i>GORDAVEXA</div>
  <h1 class="abs headline cover-title">Driving innovation<br>in <span class="hl-teal">automotive</span><br><span class="hl-orange">manufacturing</span></h1>
  <p class="abs cover-sub">Simulation Services &amp; Smart<br>Manufacturing Solutions</p>
  <div class="photo" role="img" aria-label="Black and white close-up of a dark sports car's headlight and front wheel"
       style="left:217px;top:0;width:210px;height:240px;background:radial-gradient(ellipse at 60% 40%,#6e6e6e 0%,#2a2a2a 45%,#050505 100%)"></div>
  <div class="cover-bottom"></div>
</section>

<!-- Table of contents -->
<section class="slide col-r row-1">
  <div class="bar-top"></div><div class="bar-side"></div>
  <div class="brand"><i></i>GORDAVEXA</div>
  <svg class="frame" style="left:68px;top:56px" width="292" height="162" viewBox="0 0 292 162">
    <polygon points="0.5,0.5 291.5,0.5 291.5,147 277,161.5 0.5,161.5" fill="none" stroke="var(--orange)" stroke-width="1"/>
  </svg>
  <h2 class="abs headline center toc-title">Table of <span class="hl-orange">contents</span></h2>
  <div class="toc-row" style="top:116px"><span>Introduction</span><b>02</b></div>
  <div class="toc-row" style="top:134px"><span>Agenda</span><b>04</b></div>
  <div class="toc-row" style="top:151px"><span>How We Manufacture</span><b>06</b></div>
  <div class="toc-row" style="top:169px"><span>Statistics</span><b>08</b></div>
  <div class="toc-row" style="top:187px"><span>Q&amp;A</span><b>10</b></div>
</section>

<!-- Agenda -->
<section class="slide col-l row-2">
  <div class="bar-top"></div><div class="bar-side"></div>
  <div class="brand"><i></i>GORDAVEXA</div>
  <h2 class="abs headline center section-title">Meeting <span class="hl-orange">agenda</span></h2>
  <div class="time-tag" style="left:52px">9.00<br>A.M</div>
  <div class="time-tag" style="left:185px">9.30<br>A.M</div>
  <div class="time-tag" style="left:320px">10.00<br>A.M</div>
  <div class="agenda-item" style="left:30px"><h3>Introduction &amp;<br>Company Overview</h3>
    <p>Get to know Gordavexa — our mission, our team, and how we bring simulation and innovation to the automotive manufacturing sector.</p></div>
  <div class="agenda-item" style="left:163px"><h3>Technical Deep Dive:<br>Simulation Workflows</h3>
    <p>Explore the technologies behind our simulation services and software tools. Includes live demonstration of a stamping simulation optimization loop.</p></div>
  <div class="agenda-item" style="left:298px"><h3>Use Cases &amp;<br>Q&amp;A</h3>
    <p>See real-world case studies showcasing tangible production improvements, followed by an open Q&amp;A session with our technical experts.</p></div>
</section>

<!-- Who we are -->
<section class="slide col-r row-2">
  <div class="bar-top"></div><div class="bar-side"></div>
  <div class="brand"><i></i>GORDAVEXA</div>
  <div class="tag-label">Who we are</div>
  <div class="photo" role="img" aria-label="Dark sedan on a wet road with hills under a cloudy purple sky"
       style="left:132px;top:56px;width:163px;height:83px;clip-path:polygon(12px 0,100% 0,100% 100%,0 100%,0 12px);
       background:linear-gradient(180deg,#8a8591 0%,#6f6a78 45%,#4b4a40 62%,#333028 100%)"></div>
  <h2 class="abs headline center who-title"><span class="hl-orange">Leader</span> in auto-manufacturing</h2>
  <p class="body-center" style="top:182px">Gordavexa is a leader in simulation-driven manufacturing optimization.<br>We empower automotive manufacturers with advanced simulation services and intuitive software<br>tools to reduce downtime, improve efficiency, and streamline production workflows.</p>
</section>

<!-- How we perform -->
<section class="slide col-l row-3">
  <div class="bar-top"></div><div class="bar-side"></div>
  <div class="brand"><i></i>GORDAVEXA</div>
  <div class="tag-label">Our goals</div>
  <h2 class="abs headline center section-title">How we <span class="hl-orange">perform</span></h2>
  <p class="body-center" style="top:86px">At Gordavexa, our goals drive everything we do.<br>We aim to revolutionize automotive manufacturing through smart simulation,<br>empowering our partners with the tools and insights to lead the future of production.</p>

  <svg class="icon-box" style="left:55px" viewBox="0 0 55 39">
    <polygon points="0.5,0.5 54.5,0.5 54.5,30 46,38.5 0.5,38.5" fill="#fff" stroke="var(--orange)"/>
    <g fill="none" stroke="var(--teal)" stroke-width="1">
      <circle cx="27.5" cy="18" r="10" stroke-dasharray="3 2"/>
      <circle cx="27.5" cy="17" r="5"/><path d="M25.5 22v4h4v-4"/>
    </g>
  </svg>
  <svg class="icon-box" style="left:186px" viewBox="0 0 55 39">
    <polygon points="0.5,0.5 54.5,0.5 54.5,30 46,38.5 0.5,38.5" fill="#fff" stroke="var(--orange)"/>
    <g fill="none" stroke="var(--teal)" stroke-width="1">
      <path d="M30 8a11 11 0 1 1-11 11"/><path d="M30 8v11h11"/>
      <rect x="15" y="21" width="3" height="7"/><rect x="20" y="18" width="3" height="10"/><rect x="25" y="23" width="3" height="5"/>
    </g>
  </svg>
  <svg class="icon-box" style="left:321px" viewBox="0 0 55 39">
    <polygon points="0.5,0.5 54.5,0.5 54.5,30 46,38.5 0.5,38.5" fill="#fff" stroke="var(--orange)"/>
    <g fill="none" stroke="var(--teal)" stroke-width="1">
      <circle cx="27.5" cy="17" r="11" stroke-dasharray="14 4"/>
      <circle cx="27.5" cy="14" r="3"/><path d="M22 22c1-4 10-4 11 0"/>
      <path d="M17 26h8l6-2"/>
    </g>
  </svg>
  <div class="goal-label" style="left:38px">Innovation in<br>Manufacturing</div>
  <div class="goal-label" style="left:169px">Data-Driven<br>Optimization</div>
  <div class="goal-label" style="left:303px">Customer<br>Empowerment</div>
</section>

<!-- Q&A -->
<section class="slide col-r row-3">
  <div class="bar-top"></div><div class="bar-side"></div>
  <div class="brand"><i></i>GORDAVEXA</div>
  <h2 class="abs headline center section-title">Question &amp; <span class="hl-orange">answers</span></h2>
  <svg class="frame" style="left:68px;top:93px" width="292" height="125" viewBox="0 0 292 125">
    <polygon points="0.5,0.5 291.5,0.5 291.5,111 277,124.5 0.5,124.5" fill="none" stroke="var(--orange)" stroke-width="1"/>
  </svg>
  <div class="qa-num">01.</div>
  <p class="qa-q">How does Gordavexa’s simulation service integrate with existing manufacturing workflows?</p>
  <div class="qa-rule"></div>
  <p class="qa-a">Our simulation tools are designed to plug seamlessly into your current CAD/CAM processes. We support major file formats and tailor our solutions to your production setup, enabling virtual validation of tooling without disrupting your existing workflow. This ensures faster deployment and measurable ROI from day one.</p>
</section>

<!-- Advantage -->
<section class="slide col-l row-4">
  <div class="photo" role="img" aria-label="Orange supercar driving on a seaside bridge road under a pale sky"
       style="left:0;top:0;width:427px;height:240px;background:linear-gradient(180deg,#c9dbe0 0%,#dfe6e2 40%,#9aa7ab 62%,#4d5a60 78%,#2c3236 100%)"></div>
  <div class="photo" role="img" aria-label="Red-orange sports car body"
       style="left:105px;top:145px;width:170px;height:80px;border-radius:40% 45% 10% 10%;background:radial-gradient(ellipse at 45% 50%,#d2491f 0%,#8e2a12 55%,rgba(40,30,30,0) 75%)"></div>
  <div class="bar-side" style="top:115px"></div>
  <div class="brand"><i></i>GORDAVEXA</div>
  <svg class="adv-panel" viewBox="0 0 279 128">
    <polygon points="0.5,-1 278.5,-1 278.5,127.5 17,127.5 0.5,118" fill="#fff" stroke="var(--orange)" stroke-width="1"/>
  </svg>
  <h2 class="abs headline adv-title">The Gordavexa<br><span class="hl-orange">advantage</span></h2>
  <p class="abs adv-body">Gordavexa empowers manufacturers to streamline production, reduce tooling costs, and accelerate time-to-market. We deliver measurable performance gains, helping teams optimize every stage of the stamping process — from design to execution — with data-driven precision and confidence.</p>
</section>

<!-- Thank you -->
<section class="slide col-r row-4">
  <div class="bar-top"></div><div class="bar-side"></div>
  <div class="brand"><i></i>GORDAVEXA</div>
  <div class="tag-label" style="border-bottom:none">Thank you !</div>
  <h2 class="abs headline thanks-title">Let’s shape the <span class="hl-orange">future</span> of automotives together...</h2>
  <div class="photo" role="img" aria-label="Car side mirror silhouetted against a golden sunset over a fence"
       style="left:129px;top:90px;width:298px;height:150px;clip-path:polygon(26px 0,100% 0,100% 100%,0 100%,0 26px);
       background:radial-gradient(circle at 44% 55%,#fff1c4 0%,#e39a3a 10%,#7a4a1e 32%,#2a1a10 65%,#0d0906 100%)"></div>
  <div class="abs contact-head">CONTACT US</div>
  <div class="contact-line" style="top:165px">
    <svg width="7" height="6" viewBox="0 0 7 6"><rect x=".5" y=".5" width="6" height="5" fill="none" stroke="var(--teal)" stroke-width=".8"/><path d="M.5 .8 3.5 3.3 6.5 .8" fill="none" stroke="var(--teal)" stroke-width=".8"/></svg>
    hello@gordavexa.com</div>
  <div class="contact-line" style="top:179px">
    <svg width="7" height="7" viewBox="0 0 7 7"><circle cx="3.5" cy="3.5" r="3" fill="none" stroke="var(--teal)" stroke-width=".8"/><path d="M.5 3.5h6M3.5 .5c-1.6 2-1.6 4 0 6M3.5 .5c1.6 2 1.6 4 0 6" fill="none" stroke="var(--teal)" stroke-width=".6"/></svg>
    www.gordavexa.com</div>
</section>

</body>
</html>
```